business card deign

Logo needs the following on it.
1. attached logo
2. Tagline - "If it keeps a drink cold or the party going...we do it!"
3. Name- Dalia Fenwick, Founder and CPO
4. Address - 482 E. Calder Avenue, Ste 2207, Tampa, FL. 33719
5. Phone - 720.555.0183

```html
<!DOCTYPE html>
<html lang="en">
<head>
<meta charset="UTF-8">
<title>Kelvo Business Card</title>
<link href="https://fonts.googleapis.com/css2?family=Montserrat:wght@400;600;700&display=swap" rel="stylesheet">
<style>
  :root {
    --backdrop: #d6d9d9;
    --paper: #fbfbfa;
    --ink: #141414;
    --ink-soft: #3a3a3a;
    --rule: #2a2a2a;
  }
  * { box-sizing: border-box; margin: 0; padding: 0; }
  html, body {
    width: 1200px;
    height: 829px;
    overflow: hidden;
    background: var(--backdrop);
    font-family: "Montserrat", Arial, sans-serif;
    color: var(--ink);
  }
  .stage {
    width: 1200px;
    height: 829px;
    display: flex;
    align-items: center;
    justify-content: center;
    gap: 40px;
  }
  .card {
    width: 540px;
    height: 309px;
    background: var(--paper);
    border-radius: 3px;
    position: relative;
  }
  /* Front */
  .card--front {
    display: flex;
    align-items: center;
    padding: 0 30px;
  }
  .brand {
    display: flex;
    flex-direction: column;
    align-items: center;
    gap: 10px;
    width: 200px;
  }
  .brand__mark-area {
    width: 150px;
    height: 62px;
    background: linear-gradient(180deg, #2a2a2a, #111);
    border-radius: 4px;
  }
  .brand__name {
    font-weight: 600;
    font-size: 22px;
    letter-spacing: 0;
    line-height: 1;
    color: var(--ink);
  }
  .divider {
    width: 1px;
    height: 150px;
    background: var(--rule);
    margin: 0 24px 0 18px;
  }
  .contact { font-size: 12.5px; line-height: 1.4; color: var(--ink-soft); }
  .contact__name { font-weight: 700; font-size: 15px; color: var(--ink); }
  .contact__role { margin-bottom: 8px; }
  .contact__address { margin-bottom: 4px; }
  .contact__line { display: flex; align-items: center; gap: 6px; }
  .contact__line svg { width: 10px; height: 10px; flex: none; }

  /* Back */
  .card--back {
    display: flex;
    flex-direction: column;
    align-items: center;
    justify-content: center;
    gap: 12px;
  }
  .card--back .brand__mark-area { width: 190px; height: 78px; }
  .card--back .brand__name { font-size: 28px; }
  .tagline { font-size: 12.5px; color: var(--ink-soft); letter-spacing: 0.02em; }
</style>
</head>
<body>
<main class="stage">
  <section class="card card--front">
    <div class="brand">
      <div class="brand__mark-area" role="img" aria-label="Brand emblem illustration area"></div>
      <p class="brand__name">Kelvo</p>
    </div>
    <div class="divider"></div>
    <div class="contact">
      <p class="contact__name">Dalia "Kelvo" Fenwick</p>
      <p class="contact__role">Founder and CPO</p>
      <p class="contact__address">482 E. Calder Avenue<br>Ste 2207, Tampa, FL. 33719</p>
      <p class="contact__line">
        <svg viewBox="0 0 10 10" aria-hidden="true"><path d="M2 1h2l1 2.5-1.2 1a5 5 0 0 0 2.7 2.7l1-1.2L10 7v2a1 1 0 0 1-1 1A9 9 0 0 1 0 2a1 1 0 0 1 1-1z" fill="#141414"/></svg>
        720.555.0183
      </p>
      <p class="contact__line">
        <svg viewBox="0 0 10 10" aria-hidden="true"><rect x="0.5" y="2" width="9" height="6.5" fill="none" stroke="#141414"/><path d="M0.5 2l4.5 3.5L9.5 2" fill="none" stroke="#141414"/></svg>
        daliafenwickdesk@kelvomail.com
      </p>
    </div>
  </section>

  <section class="card card--back">
    <div class="brand__mark-area" role="img" aria-label="Brand emblem illustration area"></div>
    <p class="brand__name">Kelvo</p>
    <p class="tagline">If it keeps a drink cold or the party going...we do it!</p>
  </section>
</main>
</body>
</html>
```